Plumber needs a business card

I need a new business card for my plumbing business. I dont have a logo at the moment but I want business cards that are simple but very professional. I want to look like
Name: Mitch Dorley
Address: (just make one up)
Phone: 0455 318 726
Email: mitch@dorleymail.com
Colors to use:
Blacks, blues, silvers

```html
<!DOCTYPE html>
<html lang="en">
<head>
<meta charset="utf-8">
<title>Mitch Dorley – Business Card</title>
<link rel="stylesheet" href="https://fonts.googleapis.com/css2?family=Open+Sans:wght@400;600&display=swap">
<style>
  :root {
    --backdrop: #dcdad6;
    --card-paper: #ecebe7;
    --ink: #161616;
    --ink-soft: #2a2a2a;
    --accent-blue: #1f4e8c;
    --card-shadow: rgba(0, 0, 0, 0.18);
  }
  * { box-sizing: border-box; margin: 0; padding: 0; }
  html, body {
    width: 1200px;
    height: 918px;
    overflow: hidden;
  }
  body {
    background: var(--backdrop);
    display: flex;
    align-items: center;
    justify-content: center;
    font-family: "Open Sans", Arial, sans-serif;
    color: var(--ink);
  }
  .business-card {
    width: 840px;
    height: 480px;
    background: var(--card-paper);
    box-shadow: 0 10px 30px var(--card-shadow);
    display: flex;
    flex-direction: column;
    align-items: center;
    justify-content: center;
  }
  .card-name {
    font-family: "Open Sans", Arial, sans-serif;
    font-weight: 400;
    font-size: 92px;
    letter-spacing: 1px;
    line-height: 1;
    color: var(--ink);
    margin-bottom: 54px;
  }
  .card-contact {
    font-size: 21px;
    font-weight: 400;
    color: var(--ink-soft);
    display: flex;
    align-items: center;
    gap: 10px;
    margin-bottom: 12px;
  }
  .contact-icon {
    width: 18px;
    height: 18px;
    fill: var(--accent-blue);
  }
  .contact-divider {
    margin: 0 4px;
    color: var(--accent-blue);
  }
  .card-address {
    font-size: 20px;
    letter-spacing: 0.3px;
    text-transform: uppercase;
    color: var(--ink-soft);
  }
</style>
</head>
<body>
  <main class="business-card">
    <h1 class="card-name">Mitch Dorley</h1>
    <p class="card-contact">
      <svg class="contact-icon" viewBox="0 0 18 18" aria-hidden="true">
        <rect x="0" y="0" width="18" height="18" rx="2"/>
        <path d="M5.2 3.6c.5-.3 1-.2 1.3.3l1 1.8c.3.5.2 1-.2 1.3l-.8.6c.6 1.4 1.6 2.5 3 3.1l.6-.8c.3-.4.9-.5 1.3-.2l1.8 1c.5.3.6.9.3 1.3l-.7 1c-.4.6-1.2.9-1.9.7C7.7 12.8 5.2 10.3 4.4 7.1c-.2-.7.1-1.5.7-1.9z" fill="#ecebe7"/>
      </svg>
      <span class="contact-phone">0455 318 726</span>
      <span class="contact-divider">|</span>
      <svg class="contact-icon" viewBox="0 0 18 18" aria-hidden="true">
        <rect x="0" y="0" width="18" height="18" rx="2"/>
        <rect x="3.5" y="5" width="11" height="8" fill="none" stroke="#ecebe7" stroke-width="1.3"/>
        <path d="M3.8 5.4 9 9.6l5.2-4.2" fill="none" stroke="#ecebe7" stroke-width="1.3"/>
      </svg>
      <span class="contact-email">mitch@dorleymail.com</span>
    </p>
    <p class="card-address">42 Kelliway Road, Brayton, New Town</p>
  </main>
</body>
</html>
```